Ridge 4 Ridge Turbine Rentals Pty Ltd

We are a hire company based on the Gold Coast in Australia, we Hire out Generators to construction sites, music festivals, parties, fetes etc. Anywhere where power is required we can provide it.

Ridge 4 Ridge Turbine Rentals pty Ltd also provides all leads, distribution boards, Qualified Electricians to perform all connections. we offer refuelling services and mechanical services. 24Hr on call service - to an actual english speaking operator.

Slogan ''Power Anywhere Anytime"

Industry/Entity Type

Construction

Contact Information for Business Card

M: 0481265390
E: bookings@ridge4ridgeturbinerentals-example.com.au

```html
<!DOCTYPE html>
<html lang="en">
<head>
<meta charset="utf-8">
<title>Ridge 4 Ridge Turbine Rentals – Business Card</title>
<link rel="stylesheet" href="https://fonts.googleapis.com/css2?family=Arimo:wght@400;700&display=swap">
<style>
  :root {
    --page-bg: #e6e8ea;
    --card-white: #ffffff;
    --card-white-shade: #eceeef;
    --brand-blue: #2f74a8;
    --blue-deep: #175479;
    --blue-light: #8bb6cb;
    --ink: #1a1d20;
    --ink-soft: #3a3f44;
    --rule: #b9bcbf;
  }
  * { box-sizing: border-box; margin: 0; padding: 0; }
  html, body { width: 1200px; height: 1023px; overflow: hidden; }
  body {
    background: var(--page-bg);
    font-family: "Arimo", Arial, sans-serif;
    color: var(--ink);
    position: relative;
  }
  .card {
    position: absolute;
    left: 250px;
    width: 700px;
    height: 400px;
    border-radius: 4px;
    box-shadow: 0 10px 28px rgba(0,0,0,.18), 0 2px 6px rgba(0,0,0,.12);
    overflow: hidden;
  }
  /* Front */
  .card-front {
    top: 70px;
    background: linear-gradient(160deg, var(--card-white) 0%, var(--card-white-shade) 100%);
  }
  .front-brand {
    position: absolute;
    left: 32px;
    top: 0;
    width: 250px;
    height: 100%;
    display: flex;
    align-items: center;
    gap: 12px;
  }
  .brand-dot {
    flex: none;
    width: 40px;
    height: 40px;
    border-radius: 50%;
    background: var(--brand-blue);
  }
  .brand-name {
    font-weight: 700;
    font-size: 19px;
    line-height: 1.15;
    letter-spacing: .4px;
    text-transform: uppercase;
    color: var(--ink);
  }
  .front-divider {
    position: absolute;
    left: 300px;
    top: 40px;
    width: 1px;
    height: 320px;
    background: linear-gradient(to bottom, transparent, var(--rule) 20%, var(--rule) 80%, transparent);
  }
  .front-details {
    position: absolute;
    left: 328px;
    top: 58px;
    right: 30px;
  }
  .person-name {
    font-weight: 700;
    font-size: 26px;
    color: var(--brand-blue);
  }
  .person-role {
    font-size: 16px;
    color: var(--ink-soft);
    margin-top: 4px;
  }
  .contact-list {
    list-style: none;
    margin-top: 36px;
    font-size: 12px;
    color: var(--ink-soft);
  }
  .contact-list li {
    display: flex;
    align-items: center;
    gap: 8px;
    margin-bottom: 6px;
    white-space: nowrap;
  }
  .contact-icon { width: 13px; height: 13px; flex: none; fill: var(--blue-deep); }
  .address {
    margin-top: 38px;
    font-size: 15px;
    line-height: 1.35;
    color: var(--ink-soft);
  }
  /* Back */
  .card-back {
    top: 553px;
    background: linear-gradient(165deg, var(--blue-deep) 0%, #3f7fa3 55%, var(--blue-light) 100%);
    display: flex;
    align-items: center;
    justify-content: center;
    gap: 16px;
  }
  .card-back .brand-dot { background: var(--ink); width: 50px; height: 50px; }
  .card-back .brand-name { font-size: 28px; }
</style>
</head>
<body>
  <section class="card card-front" aria-label="Business card front">
    <div class="front-brand">
      <span class="brand-dot"></span>
      <span class="brand-name">Ridge 4 Ridge<br>Turbine Rentals</span>
    </div>
    <div class="front-divider"></div>
    <div class="front-details">
      <p class="person-name">Alex Carter</p>
      <p class="person-role">Managirg Director</p>
      <ul class="contact-list">
        <li>
          <svg class="contact-icon" viewBox="0 0 16 16"><path d="M3.5 1l3 3-1.6 2a9 9 0 0 0 5.1 5.1l2-1.6 3 3-2 2.5C6.5 14.7 1.3 9.5.8 3z"/></svg>
          0481265390
        </li>
        <li>
          <svg class="contact-icon" viewBox="0 0 16 16"><path d="M1 3h14v10H1z M1 3l7 6 7-6" fill="none" stroke="#175479" stroke-width="1.6"/></svg>
          bookings@ridge4ridgeturbinerentals-example.com.au
        </li>
        <li>
          <svg class="contact-icon" viewBox="0 0 16 16"><g fill="none" stroke="#175479" stroke-width="1.3"><circle cx="8" cy="8" r="6.5"/><ellipse cx="8" cy="8" rx="2.8" ry="6.5"/><path d="M1.5 8h13M3 4.5h10M3 11.5h10"/></g></svg>
          www.ridge4ridgeturbinerentals-example.com.au
        </li>
      </ul>
      <p class="address">Here your company<br>or home address</p>
    </div>
  </section>

  <section class="card card-back" aria-label="Business card back">
    <span class="brand-dot"></span>
    <span class="brand-name">Ridge 4 Ridge<br>Turbine Rentals</span>
  </section>
</body>
</html>
```